hi,
we need a Logo designed for our new Beef Jerky Products. We are currently operating as a Butcher Shop but are expanding to include Small Goods. Our current name is Crown of Cuts, so we would like our new name to be Crown of Cuts - Beef Jerky. As I have different Products and Flavours, we need a section that we can change flavour names. On the Label I need the following information:
* Room for a barcode.
* Nutritional Panel with Ingredients Section
* Able for us to modify Flavour Panel, Ingredient Panel
* Portrait Style
* Able to be descale size of label, as I have different size packets
* To stand out on the Supermarket Shelf (not fluro colours though)
* PRODUCT OF AUSTRALIA
PACKED BY CROWN OF CUTS
27 Palton Rd
Ashby Flats
Mackay QLD 4799
PH 07 48213096
* Find us on Chatter Symbol
* High Protein Low Fat Full Flavour 100% Australian Beef.
* If it suits, I had in my head a fancy K symbol watermarked in the background. Only if it suits your design.
I have uploaded our current crown of cuts Logo, but use this only as I guide, I am open to other options as I would like something what captures the customer - Eye Catching.
Thank You.
Ned.

```html
<!DOCTYPE html>
<html lang="en">
<head>
<meta charset="utf-8">
<title>Crown of Cuts – Beef Jerky Label</title>
<link rel="stylesheet" href="https://fonts.googleapis.com/css2?family=Arimo:wght@400;700&family=Crimson+Text:wght@400;600&display=swap">
<style>
  :root {
    --stage: #3a3a3c;
    --brown-deep: #2a170d;
    --brown: #3d2416;
    --brown-warm: #5a3620;
    --gold: #f5c02e;
    --gold-soft: #ffd24a;
    --cream: #f2efe9;
    --silver: #d9d9d9;
    --ink: #111111;
    --white: #ffffff;
  }
  * { box-sizing: border-box; margin: 0; padding: 0; }
  html, body { width: 1200px; height: 1000px; overflow: hidden; }
  body { background: var(--stage); font-family: "Arimo", Arial, sans-serif; position: relative; }

  /* ---------- Front label ---------- */
  .label-front {
    position: absolute; left: 22px; top: 62px; width: 574px; height: 764px;
    background: radial-gradient(ellipse at 45% 35%, var(--brown-warm) 0%, var(--brown) 45%, var(--brown-deep) 100%);
    overflow: hidden;
  }
  .front-art { position: absolute; inset: 0; }
  .monogram {
    position: absolute; left: 80px; top: 110px; width: 300px; height: 340px;
    border-radius: 40%;
    background: radial-gradient(ellipse at center, rgba(245,192,46,0.55) 0%, rgba(245,192,46,0.15) 60%, rgba(245,192,46,0) 75%);
  }
  .flavour-panel {
    position: absolute; left: 38px; top: 523px; width: 156px; height: 93px;
    background: var(--brown-deep);
    border: 3px solid var(--gold);
    border-radius: 14px;
    box-shadow: 0 0 0 3px var(--brown);
  }
  .brand-plate {
    position: absolute; left: 328px; top: 468px; width: 216px; height: 150px;
    background: var(--brown-deep);
    border: 3px solid var(--gold);
    border-radius: 18px;
    box-shadow: 0 0 0 4px var(--brown);
    display: flex; align-items: center; justify-content: center; text-align: center;
  }
  .brand-name {
    font-family: "Crimson Text", Georgia, serif; font-weight: 600;
    color: var(--cream); font-size: 34px; line-height: 1.05;
  }
  .claims {
    position: absolute; right: 28px; top: 638px; text-align: right;
    color: var(--brown-deep); font-weight: 700;
  }
  .claims .claim-main { font-size: 27px; letter-spacing: -0.2px; }
  .claims .claim-origin { font-size: 27px; margin-top: 2px; }
  .rule { position: absolute; left: 62px; right: 28px; top: 711px; height: 1px; background: #bcbcbc; }
  .origin-band {
    position: absolute; left: 0; right: 0; top: 722px; height: 28px;
    background: var(--brown-deep); color: var(--gold);
    font-size: 20px; text-align: center; line-height: 28px;
  }
  .base-strip { position: absolute; left: 0; right: 0; top: 750px; bottom: 0; background: var(--silver); }

  /* ---------- Back label ---------- */
  .label-back {
    position: absolute; left: 622px; top: 235px; width: 554px; height: 735px;
    background: radial-gradient(ellipse at 50% 45%, var(--brown-warm) 0%, var(--brown) 50%, var(--brown-deep) 100%);
    border-left: 12px solid var(--gold);
  }
  .nutrition {
    position: absolute; left: 92px; top: 23px; width: 346px; height: 429px;
    background: var(--white); padding: 12px 14px;
  }
  .nutrition-inner { border: 2px solid var(--ink); height: 100%; padding: 4px 6px; color: var(--ink); font-size: 15px; line-height: 1.2; overflow: hidden; }
  .nutrition h2 { font-size: 33px; font-weight: 700; line-height: 1; margin-bottom: 4px; letter-spacing: -0.3px; }
  .bar-thick { height: 10px; background: var(--ink); margin: 2px 0; }
  .bar-mid { height: 6px; background: var(--ink); margin: 2px 0; }
  .row { display: flex; justify-content: space-between; border-top: 1px solid var(--ink); padding: 0; }
  .row.no-line { border-top: none; }
  .row.value-head { justify-content: flex-end; font-size: 14px; }
  .row b { font-weight: 700; }
  .row.indent span:first-child { padding-left: 12px; }
  .fine { font-size: 12px; line-height: 1.25; }
  .fine-line { border-top: 1px solid var(--ink); }

  .address {
    position: absolute; left: 41px; top: 548px; font-style: normal;
    color: var(--gold); font-weight: 700; font-size: 18px; line-height: 24.5px;
  }
  .social { position: absolute; left: 41px; top: 688px; display: flex; align-items: center; gap: 12px; color: var(--gold); font-weight: 700; font-size: 18px; }
  .barcode-space {
    position: absolute; left: 232px; top: 639px; width: 240px; height: 84px;
    background: var(--white); border: 2px solid var(--ink);
    display: flex; align-items: center; justify-content: center;
    font-size: 22px; color: var(--ink);
  }
  .packed-by {
    position: absolute; left: 517px; top: 370px;
    transform: translate(-50%, -50%) rotate(-90deg);
    white-space: nowrap; color: var(--gold); font-weight: 700; font-size: 29px; letter-spacing: 0.3px;
  }
</style>
</head>
<body>

<section class="label-front">
  <svg class="front-art" width="574" height="764" viewBox="0 0 574 764" aria-hidden="true">
    <path d="M0 470 C120 560 360 560 574 420 L574 520 C430 610 160 620 0 520 Z" fill="#e6a41f"/>
    <path d="M0 505 C150 600 400 590 574 470 L574 764 L0 764 Z" fill="#f4f4f4"/>
    <path d="M0 560 C200 640 420 620 574 560 L574 764 L0 764 Z" fill="#ececec"/>
    <path d="M574 340 L470 470 L574 420 Z" fill="#e6a41f"/>
  </svg>
  <div class="monogram" role="img" aria-label="Large crowned script monogram letter in gold"></div>
  <div class="flavour-panel" aria-label="Flavour name panel"></div>
  <div class="brand-plate"><span class="brand-name">Crown of Cuts<br>Beef Jerky</span></div>
  <div class="claims">
    <p class="claim-main">High Protein Low Fat Full Flavour</p>
    <p class="claim-origin">100% Australian Beef.</p>
  </div>
  <div class="rule"></div>
  <div class="origin-band">Product Of Australia</div>
  <div class="base-strip"></div>
</section>

<section class="label-back">
  <div class="nutrition">
    <div class="nutrition-inner">
      <h2>Nutrition Facts</h2>
      <div>Serving Size 4 oz (112g)<br>raw, as packaged.<br>Servings Per Container varied</div>
      <div class="bar-thick"></div>
      <div class="row no-line"><span>Amount Per Serving</span></div>
      <div class="row"><span><b>Calories</b> 150</span><span>Calories from Fat 50</span></div>
      <div class="bar-mid"></div>
      <div class="row no-line value-head">% Daily Value*</div>
      <div class="row"><span><b>Total Fat</b> 6g</span><b>9%</b></div>
      <div class="row indent"><span>Saturated Fat 2.5g</span><b>13%</b></div>
      <div class="row"><span><b>Cholesterol</b> 70mg</span><b>23%</b></div>
      <div class="row"><span><b>Sodium</b> 75mg</span><b>3%</b></div>
      <div class="row"><span><b>Total Carbohydrate</b> 0g</span><b>0%</b></div>
      <div class="row"><span><b>Protein</b> 24g</span><b>48%</b></div>
      <div class="bar-thick"></div>
      <div class="row no-line"><span>Iron 15%</span><span>•</span></div>
      <div class="fine fine-line">Not a significant source of dietary fiber,<br>sugars, vitamin A, vitamin C, and calcium</div>
      <div class="fine fine-line">* Percent Daily Values are based on a 2,000-<br>calorie diet</div>
    </div>
  </div>

  <address class="address">
    27 Palton Rd<br>Ashby Flats<br>Mackay QLD 4799<br>PH 07 48213096
  </address>
  <div class="social"><span>Find us on</span><span>Chatter</span></div>
  <div class="barcode-space">Barcode</div>
  <div class="packed-by">PACKED BY CROWN OF CUTS</div>
</section>

</body>
</html>
```